Business Card Project

We are a small consulting firm. You can experiment with any design.
Must have:
1) Company name - OLUNDEX International
2) Company slogan - simple solutions for complex problems
3) Name/Title/Phone/Email/WWW/ - use anything you like as an example.

Industry/Entity Type

Business

```html
<!DOCTYPE html>
<html lang="en">
<head>
<meta charset="utf-8">
<title>OLUNDEX International – Business Card</title>
<link rel="stylesheet" href="https://fonts.googleapis.com/css2?family=Montserrat:wght@400&family=Open+Sans:wght@400;700&display=swap">
<style>
  :root {
    --page: #eceff2;
    --blue-deep: #0b6fbe;
    --blue-mid: #1a8ad3;
    --blue-light: #2eaee6;
    --white: #ffffff;
    --ink-grey: #5e6266;
    --divider: rgba(255,255,255,0.55);
  }
  * { margin: 0; padding: 0; box-sizing: border-box; }
  html, body { width: 1200px; height: 900px; overflow: hidden; }
  body {
    background: var(--page);
    font-family: "Open Sans", Arial, sans-serif;
    display: flex;
    flex-direction: column;
    align-items: center;
    justify-content: center;
    gap: 50px;
  }
  .card {
    position: relative;
    width: 640px;
    height: 366px;
    border-radius: 26px;
    overflow: hidden;
    box-shadow: 0 6px 18px rgba(0,0,0,0.18);
  }

  /* Front */
  .card-front {
    background: radial-gradient(circle at 40% 45%, var(--blue-mid) 0%, var(--blue-deep) 55%, var(--blue-light) 130%);
  }
  .front-logo {
    position: absolute;
    left: 150px;
    top: 118px;
    display: flex;
    align-items: center;
    gap: 18px;
    color: var(--white);
  }
  .logo-dot {
    width: 54px; height: 54px; border-radius: 50%;
    background: currentColor;
    flex: none;
  }
  .logo-words { font-family: "Montserrat", Arial, sans-serif; font-weight: 400; line-height: 1; }
  .logo-name { font-size: 58px; letter-spacing: 1px; display: block; }
  .logo-sub { font-size: 15px; letter-spacing: 8.5px; display: block; margin-top: 4px; }
  .front-web {
    position: absolute;
    left: 222px;
    top: 212px;
    color: var(--white);
    font-size: 15px;
    white-space: nowrap;
  }

  /* Back */
  .card-back { background: var(--white); }
  .back-shapes { position: absolute; inset: 0; width: 100%; height: 100%; }
  .back-logo {
    position: absolute;
    left: 44px;
    top: 92px;
    display: flex;
    align-items: center;
    gap: 16px;
    color: var(--ink-grey);
  }
  .back-logo .logo-dot { width: 48px; height: 48px; background: var(--blue-mid); }
  .back-logo .logo-name { font-size: 52px; }
  .back-logo .logo-sub { font-size: 14px; letter-spacing: 7.4px; }
  .holder {
    position: absolute;
    left: 40px;
    bottom: 30px;
    color: var(--white);
    white-space: nowrap;
  }
  .holder-name { font-size: 19px; font-weight: 700; }
  .holder-title { font-size: 12px; font-weight: 700; }
  .holder-web { font-size: 15px; margin-top: 2px; }
  .contact {
    position: absolute;
    right: 24px;
    top: 206px;
    color: var(--white);
    font-size: 14px;
    line-height: 1.6;
    padding-left: 18px;
    border-left: 1px solid var(--divider);
    white-space: nowrap;
  }
  .contact-row { display: flex; align-items: center; gap: 7px; }
  .contact-row svg { width: 12px; height: 12px; fill: var(--white); flex: none; }
  .slogan {
    position: absolute;
    right: 24px;
    bottom: 42px;
    color: var(--white);
    font-size: 14px;
    white-space: nowrap;
  }
</style>
</head>
<body>

  <section class="card card-front" aria-label="Business card front">
    <div class="front-logo">
      <span class="logo-dot"></span>
      <span class="logo-words">
        <span class="logo-name">OLUNDEX</span>
        <span class="logo-sub">INTERNATIONAL</span>
      </span>
    </div>
    <p class="front-web">www.webname.com</p>
  </section>

  <section class="card card-back" aria-label="Business card back">
    <svg class="back-shapes" viewBox="0 0 640 366" preserveAspectRatio="none" aria-hidden="true">
      <defs>
        <linearGradient id="backBlue" x1="0" y1="1" x2="1" y2="0">
          <stop offset="0" stop-color="#2eaee6"/>
          <stop offset="1" stop-color="#0b6fbe"/>
        </linearGradient>
        <linearGradient id="bandGrey" x1="1" y1="0" x2="0" y2="1">
          <stop offset="0" stop-color="#6f7275"/>
          <stop offset="1" stop-color="#b9bbbd" stop-opacity="0"/>
        </linearGradient>
      </defs>
      <path d="M250,366 C420,300 556,170 566,0 L600,0 C592,170 460,300 290,366 Z" fill="url(#bandGrey)"/>
      <path d="M0,270 C300,300 560,180 590,0 L640,0 L640,366 L0,366 Z" fill="url(#backBlue)"/>
    </svg>

    <div class="back-logo">
      <span class="logo-dot"></span>
      <span class="logo-words">
        <span class="logo-name">OLUNDEX</span>
        <span class="logo-sub">INTERNATIONAL</span>
      </span>
    </div>

    <div class="holder">
      <p><span class="holder-name">Your Name</span> <span class="holder-title">| Job Title</span></p>
      <p class="holder-web">www.webname.com</p>
    </div>

    <div class="contact">
      <p class="contact-row">
        <svg viewBox="0 0 24 24" aria-hidden="true"><path d="M6.6 10.8a15 15 0 0 0 6.6 6.6l2.2-2.2c.3-.3.7-.4 1-.2 1.1.4 2.3.6 3.6.6.6 0 1 .4 1 1V20c0 .6-.4 1-1 1A17 17 0 0 1 3 4c0-.6.4-1 1-1h3.5c.6 0 1 .4 1 1 0 1.3.2 2.5.6 3.6.1.3 0 .7-.2 1z"/></svg>
        000-000-000
      </p>
      <p class="contact-row">
        <svg viewBox="0 0 24 24" aria-hidden="true"><path d="M2 5h20v14H2z M3.5 6.5 12 13l8.5-6.5" fill="none" stroke="#fff" stroke-width="2"/></svg>
        name@domainname.com
      </p>
    </div>

    <p class="slogan">simple solutions for complex problems</p>
  </section>

</body>
</html>
```